Labour Day banner showcasing 20% off site

Banner graphic promoting our Labour Day sale
Size: 2000px x 600px
- examples from other companies and their sale banners have been uploaded for inspiration. Labour day examples are for the United States's holiday and submissions should NOT be in their country colours.
- product images can be found at www.tallpinegreens.com

Target Market(s)

19+

Industry/Entity Type

Cannabis

Requirements
Must have
• Phrases:
- “Happy Labour Day”
- “20% off site wide sale*"
- "Coupon code: Harvest20"
- Underneath phrase the date of sale “September 3rd - 7th”
- In tiny print “*excludes all sale and bundled items”
- MUST BE 2000px x 600px
Nice to have
• - images of the products or bud we carry which can be found at www.tallpinegreens.com
- bold
Should not have
• - company logo
- the American flag, we are a Canadian company, colours and flag should all be Canadian

```html
<!DOCTYPE html>
<html lang="en">
<head>
<meta charset="utf-8">
<title>Happy Labour Day Sale Banner</title>
<link href="https://fonts.googleapis.com/css2?family=Bebas+Neue&family=Open+Sans:ital,wght@1,600;1,700&display=swap" rel="stylesheet">
<style>
  :root {
    --page-bg: #c2e3d4;
    --ink-white: #ffffff;
    --ink-dark: #111111;
    --band-blue: #2a5670;
    --band-slate: #47606f;
    --band-green: #2f6a32;
    --band-lime: #4f7d2a;
    --bud-tone: #5a6670;
    --leaf-tone: #3f6b3c;
  }
  html, body {
    margin: 0;
    padding: 0;
    width: 1200px;
    height: 1200px;
    overflow: hidden;
    background: var(--page-bg);
  }
  .canvas {
    position: relative;
    width: 1200px;
    height: 1200px;
  }
  .banner {
    position: absolute;
    left: 80px;
    top: 462px;
    width: 1042px;
    height: 311px;
    overflow: hidden;
    background:
      radial-gradient(ellipse 420px 240px at 640px 230px, rgba(95,135,40,0.75), transparent 70%),
      linear-gradient(180deg, var(--band-slate) 0%, var(--band-blue) 45%, #285a56 70%, var(--band-green) 100%);
    box-shadow: 3px 4px 6px rgba(0,0,0,0.35);
  }
  .bud-photo {
    position: absolute;
    left: 56px;
    top: 62px;
    width: 230px;
    height: 246px;
    border-radius: 48% 52% 45% 55% / 55% 50% 50% 45%;
    background: radial-gradient(ellipse at 45% 45%, #6d7a82 0%, var(--bud-tone) 55%, #3f5448 100%);
    opacity: 0.9;
  }
  .leaf-photo {
    position: absolute;
    right: 0;
    top: 0;
    width: 330px;
    height: 311px;
    background: radial-gradient(ellipse at 60% 50%, rgba(63,107,60,0.55) 0%, rgba(63,107,60,0.2) 55%, transparent 80%);
  }
  .headline {
    position: absolute;
    left: 0;
    right: 0;
    top: 8px;
    display: flex;
    justify-content: center;
    align-items: center;
    gap: 28px;
  }
  .headline h1 {
    margin: 0;
    font-family: "Bebas Neue", sans-serif;
    font-weight: 400;
    font-size: 90px;
    line-height: 1;
    letter-spacing: 2px;
    color: var(--ink-white);
    word-spacing: 10px;
  }
  .gear { width: 58px; height: 58px; flex: none; }
  .rule {
    position: absolute;
    left: 403px;
    top: 96px;
    width: 233px;
    height: 2px;
    background: var(--ink-white);
  }
  .offer {
    position: absolute;
    left: 318px;
    top: 112px;
    display: flex;
    align-items: flex-end;
    font-family: "Bebas Neue", sans-serif;
    color: var(--ink-white);
  }
  .offer .percent { font-size: 86px; line-height: 0.82; }
  .offer .text { font-size: 50px; line-height: 0.8; margin-left: 6px; padding-bottom: 12px; }
  .coupon {
    position: absolute;
    left: 470px;
    top: 183px;
    width: 96px;
    height: 44px;
    border: 1.5px solid var(--ink-white);
    border-radius: 2px;
    box-sizing: border-box;
    text-align: center;
    font-family: "Bebas Neue", sans-serif;
  }
  .coupon .label {
    display: block;
    color: var(--ink-white);
    font-size: 14px;
    line-height: 18px;
  }
  .coupon .code {
    display: block;
    margin: 0 3px;
    background: var(--ink-white);
    color: var(--ink-dark);
    font-size: 20px;
    line-height: 20px;
  }
  .dates {
    position: absolute;
    left: 0;
    right: 0;
    top: 236px;
    text-align: center;
    font-family: "Open Sans", sans-serif;
    font-style: italic;
    font-weight: 600;
    font-size: 27px;
    color: var(--ink-white);
  }
  .fine-print {
    position: absolute;
    left: 0;
    right: 0;
    top: 284px;
    text-align: center;
    font-family: "Open Sans", sans-serif;
    font-style: italic;
    font-weight: 700;
    font-size: 10px;
    color: var(--ink-white);
  }
</style>
</head>
<body>
<div class="canvas">
  <section class="banner">
    <div class="leaf-photo" role="img" aria-label="Faint photo of cannabis leaves"></div>
    <div class="bud-photo" role="img" aria-label="Photo of a cannabis bud"></div>

    <div class="headline">
      <svg class="gear" viewBox="0 0 60 60" aria-hidden="true">
        <g fill="#ffffff">
          <rect x="25" y="2" width="10" height="12" rx="1"/>
          <rect x="25" y="46" width="10" height="12" rx="1"/>
          <rect x="2" y="25" width="12" height="10" rx="1"/>
          <rect x="46" y="25" width="12" height="10" rx="1"/>
          <rect x="25" y="2" width="10" height="12" rx="1" transform="rotate(45 30 30)"/>
          <rect x="25" y="2" width="10" height="12" rx="1" transform="rotate(135 30 30)"/>
          <rect x="25" y="2" width="10" height="12" rx="1" transform="rotate(225 30 30)"/>
          <rect x="25" y="2" width="10" height="12" rx="1" transform="rotate(315 30 30)"/>
          <circle cx="30" cy="30" r="20"/>
        </g>
        <circle cx="30" cy="30" r="14" fill="#2f5c68"/>
      </svg>
      <h1>Happy Labour Day</h1>
      <svg class="gear" viewBox="0 0 60 60" aria-hidden="true">
        <g fill="#ffffff">
          <rect x="25" y="2" width="10" height="12" rx="1"/>
          <rect x="25" y="46" width="10" height="12" rx="1"/>
          <rect x="2" y="25" width="12" height="10" rx="1"/>
          <rect x="46" y="25" width="12" height="10" rx="1"/>
          <rect x="25" y="2" width="10" height="12" rx="1" transform="rotate(45 30 30)"/>
          <rect x="25" y="2" width="10" height="12" rx="1" transform="rotate(135 30 30)"/>
          <rect x="25" y="2" width="10" height="12" rx="1" transform="rotate(225 30 30)"/>
          <rect x="25" y="2" width="10" height="12" rx="1" transform="rotate(315 30 30)"/>
          <circle cx="30" cy="30" r="20"/>
        </g>
        <circle cx="30" cy="30" r="14" fill="#2f5c68"/>
      </svg>
    </div>

    <div class="rule"></div>

    <div class="offer">
      <span class="percent">20%</span>
      <span class="text">Off Site Wide Sale</span>
    </div>

    <div class="coupon">
      <span class="label">Coupon Code</span>
      <span class="code">Harvest20</span>
    </div>

    <p class="dates" style="margin:0">September 3rd - 7th</p>
    <p class="fine-print" style="margin:0">Excludes all Sale and Bundled Items</p>
  </section>
</div>
</body>
</html>
```